Design a two sided Flyer for Each Porch bulk delivery from NPDS - size 8,5" x 11"

We need a flyer that will be accepted by NPDS for each porch bulk delivery (size 8,5" x 11"). It needs to be double sided designed and we have already made the copy writing. We just need a designer to make it look stunning and chique. When our potential customers receive the flyer they should have a feeling that they can improve their house with the right kind of modern lighting. The flyer should be saying in the front cozy, safety, warmth, in short everything you need at home for the winter. (and they can off course buy that at our web store). Having (happy) people on the flyer a bonus. And in the back it will give a couple tips and tricks on how you should light up your home.

We have included in attachment
- a word document with the writing that needs to go on the flyer (front and back)
- our logo in several files and formats

Under are links to our filecrate where you can find many pictures of the lamps we sell but feel free to find others.
- https://www.filecrate.example/sh/qk7tn2r4pz8wvmd/h3LpQrT6Yb
- https://www.filecrate.example/sh/91bvk6sj2pf8rna/mHT5x2K7Nc
- https://www.filecrate.example/sh/pwtt4ajdm38gy6q/_82kFdR4Wq
- https://www.filecrate.example/sh/vnc38sdqe40717h/_pzRtMjwe7

Last but not least our own site:
- http://www.brenovaka.example

Target Market(s)

USA Families in the age of 25-45y old. Medium to high income and open minded

Industry/Entity Type

House

Requirements
Must have
• - minimum of 350 dpi (dot per inch) resolution.
- size 8.5" x 11"
- two sided
- should grab the attention of the reader and give a sense of class, cozy and warmth
Should not have
• no cheap looking, screaming words, flyer

```html
<!DOCTYPE html>
<html lang="en">
<head>
<meta charset="utf-8">
<title>Your guide to the perfect interior lighting</title>
<link href="https://fonts.googleapis.com/css2?family=EB+Garamond:wght@400;500&family=Fira+Sans:ital,wght@0,600;1,400;1,600&display=swap" rel="stylesheet">
<style>
  :root{
    --ink:#1a1a1a;
    --paper:#ffffff;
    --glow:#ece6dc;
    --green:#7cb82f;
    --brand:#e8742a;
    --rule:#1a1a1a;
  }
  html,body{margin:0;padding:0;overflow:hidden;}
  body{width:927px;height:1200px;background:var(--paper);position:relative;color:var(--ink);
    font-family:"EB Garamond",Garamond,serif;}
  .lamp-glow{position:absolute;inset:0;
    background:radial-gradient(ellipse 420px 520px at 640px 820px,#e9e2d6 0%,#f3efe9 45%,rgba(255,255,255,0) 80%),
               linear-gradient(180deg,#f7f7f7 0%,#f1f0ee 60%,#f4f3f1 100%);}
  .block{position:absolute;left:55px;width:820px;}
  .title{font-family:"Fira Sans",sans-serif;font-weight:600;font-size:24px;margin:0;top:38px;letter-spacing:-.2px;}
  .tip-heading{font-family:"Fira Sans",sans-serif;font-style:italic;font-weight:400;font-size:21.5px;margin:0;letter-spacing:-.2px;}
  .tip-heading .accent{color:var(--green);font-size:27px;}
  .calc-heading{font-family:"Fira Sans",sans-serif;font-style:italic;font-weight:600;font-size:21.5px;margin:0;top:840px;}
  .copy{font-size:15.6px;line-height:21.3px;margin:0;}
  .calc-table{position:absolute;left:55px;top:869px;width:817px;border-collapse:collapse;
    font-size:15px;line-height:17px;text-align:center;}
  .calc-table td{border:1.5px solid var(--rule);padding:2px 4px;vertical-align:top;}
  .calc-table .head-row td{height:40px;}
  .calc-table .purpose-row td{height:66px;vertical-align:middle;}
  .calc-table .purpose-row td.top{vertical-align:top;}
  .calc-table .use-row td{height:41px;}
  .calc-table .note-row td{height:20px;}
  .brand{position:absolute;right:58px;top:1150px;font-family:"Fira Sans",sans-serif;font-size:16px;color:var(--brand);}
</style>
</head>
<body>
<div class="lamp-glow" role="img" aria-label="Faint photo of a glowing spherical pendant lamp in a warm interior"></div>

<h1 class="block title">Your guide to the perfect interior lighting</h1>
<p class="block copy" style="top:76px">The best light there is, is natural light. However with the winter in-sight and daytime light shrinking, we more and more depend on artificial lights to light up our living spaces and make our homes sparkle in the dark, feel warmer, cozier and safer.&nbsp; If you’re contemplating new light fixtures for your house, here are few hints to help you choose the right luminaire:</p>

<h2 class="block tip-heading" style="top:180px">Determine what your lighting goals are.</h2>
<p class="block copy" style="top:214px">Direct or task lighting is focused in the space you are trying to work. Ambient or indirect lighting is used for ambiance and for overall lighting of a space. Once chosen you can begin to choose lighting options.&nbsp; Each room in your home should have a mood you want to set, as well as a function you want your lighting to serve. Choose the right amount of light for your room by using the calculation under.</p>

<h2 class="block tip-heading" style="top:305px">Use multiple light sources for one space.</h2>
<p class="block copy" style="top:339px">This will help you to achieve a variety of functions and activities in one space and it will reduce shadows.&nbsp; Have a mix of light sources at different levels (recessed, suspension lamps, wall scones,…) to create a flattering ambience and add appropriate task lighting for whatever you do in that space. In the kitchen, under counter lights can provide great task lighting. While in a living room, opt for a floor lamp next to a couch or favorite reading chair</p>

<h2 class="block tip-heading" style="top:430px">Choose your chandeliers wisely.</h2>
<p class="block copy" style="top:464px">Because of the central position in a space a chandelier determines largely the decorating value of it. Ask yourself if you want it to be an eye catcher or should it blend in?&nbsp; In any way and whichever is your décor choice, measure out the space, and ceiling height before ordering to ensure enough head room will be available below the hanging chandelier.</p>

<h2 class="block tip-heading" style="top:576px">Highlight the room’s highlights.</h2>
<p class="block copy" style="top:610px">Dramatize wall textures, accent artwork or light up the fireplace. Draw the attention within the space to the architecture and decorative highlights of it. You can do this with special adjustable spot lighting that is either recessed or on a track or use upwards lighting wall scones.</p>

<h2 class="block tip-heading" style="top:717px">Go for <span class="accent">green</span> and save!</h2>
<p class="block copy" style="top:760px">85% of the cost of lighting are energy costs so it pays off rather fast to switch to energy saving alternatives like LED. A little bit more expensive at the registry but far cheaper on your next energy bill. Don’t like the white color? Look on the packaging for the color temperature; 2700K is perfect for ambiance, 3000k for task lighting.</p>

<h2 class="block calc-heading">Calculate yourself how much light you really need</h2>

<table class="calc-table">
  <colgroup>
    <col style="width:180px"><col style="width:123px"><col style="width:42px"><col style="width:115px"><col style="width:125px"><col style="width:77px"><col style="width:155px">
  </colgroup>
  <tr class="head-row">
    <td>How big is the area?</td><td>Width (A)</td><td></td><td>Length(B)</td><td></td><td>Surface (A)x(B)</td><td>(C)</td>
  </tr>
  <tr class="purpose-row">
    <td class="top">What is the purpose of the area?</td>
    <td colspan="2" style="vertical-align:bottom">LED or CFLI lighting</td>
    <td>Total Lumen needed (C) x (D)</td>
    <td colspan="2">Incandescent lighting</td>
    <td class="top">Total Watt needed (C) x (E)</td>
  </tr>
  <tr class="use-row">
    <td>Relax, Watch Tv, Talk</td><td>Lumen per Sq ft (D)</td><td>20</td><td></td><td>Watt per Sq ft (E)</td><td>1.5</td><td></td>
  </tr>
  <tr class="use-row">
    <td>Have dinner, dress up</td><td>Lumen per Sq ft (D)</td><td>30</td><td></td><td>Watt per Sq ft (E)</td><td>2</td><td></td>
  </tr>
  <tr class="use-row">
    <td>Cook, Work, Read</td><td>Lumen per Sq ft (D)</td><td>50</td><td></td><td>Watt per Sq ft (E)</td><td>3.5</td><td></td>
  </tr>
  <tr class="note-row">
    <td colspan="7">Simple add up the wattage or Lumen of the light bulbs in the space to see if you meet the total light needed</td>
  </tr>
</table>

<div class="brand">brenovaka.example</div>
</body>
</html>
```